Business Card Design Project

I am looking for a minimal matte background/shiny (spot UV) ink monochromatic design with a splash of neon color.

the card should be 2 sided, logo only on one side - all info and possibly logo on the other.

My creative director described the colors he imagined for the design to be:
'it's a dark field, like charcoal or a really dark burgundy, or deep blue, shot through with a neon—but just a tiny bit of it. so a charcoal field with a laser-thin streak of electric lime, safety orange, or cobalt blue. really beautiful stuff.'

here are some samples of the types of cards I am trying to create:
http://www.snapvault.example/photos/dawnpress/4182736450/in/photostream -> Vornelle Lustre

http://www.snapvault.example/photos/dawnpress/3859201746/in/photostream -> Standard Coated (14pt/matte) with SPOT UV

http://www.snapvault.example/photos/dawnpress/3859201372/in/photostream/ -> Dense Orvane with Raised Ink

http://www.snapvault.example/photos/dawnpress/5128463907/in/photostream/ -> Standard Coated (14pt/matte) with SPOT UV

Here is my logo:
https://www.filecrate.example/s/qtrwx730pkd4zn/gulvane%20logotype%20final.ai

Here are the details for info:
Owen Carlisle Dray
email - owen@gulvane.example
mobile - 555 318 6724
web -
gulvane.example: inventive technology applications
gulvane-video.example: innovative video advertising

please let me know if there is anything at all that you need.

Target Market(s)

mid to large agencies that require interactive design and entrepreneurial/startup individuals/companies that need application development.

Industry/Entity Type

Safety

Requirements
Must have
• logo only on one side

```html
<!DOCTYPE html>
<html lang="en">
<head>
<meta charset="utf-8">
<title>Gulvane Business Card</title>
<link rel="stylesheet" href="https://fonts.googleapis.com/css2?family=Oswald:wght@400&family=Mulish:wght@400;800&display=swap">
<style>
  :root {
    --paper: #ffffff;
    --charcoal: #464646;
    --ink-white: #f4f4f4;
    --ink-black: #0a0a0a;
    --neon-orange: #f26722;
  }
  html, body {
    margin: 0;
    width: 1200px;
    height: 379px;
    overflow: hidden;
    background: var(--paper);
  }
  .sheet {
    position: relative;
    width: 1200px;
    height: 379px;
  }
  .card {
    position: absolute;
    top: 0;
    height: 379px;
    background: var(--charcoal);
  }
  .card--front { left: 0; width: 583px; }
  .card--back { left: 618px; width: 582px; }

  .wordmark {
    position: absolute;
    margin: 0;
    font-family: "Oswald", sans-serif;
    font-weight: 400;
    color: var(--ink-white);
    text-transform: uppercase;
    line-height: 1;
    white-space: nowrap;
  }
  .card--front .wordmark {
    left: 38px;
    top: 266px;
    font-size: 86px;
    letter-spacing: 0.36em;
  }
  .card--back .wordmark {
    left: 137px;
    top: 110px;
    font-size: 55px;
    letter-spacing: 0.36em;
  }
  .accent-square {
    position: absolute;
    background: var(--neon-orange);
  }
  .card--front .accent-square {
    left: 470px;
    top: 228px;
    width: 64px;
    height: 64px;
  }
  .card--back .accent-square {
    left: 432px;
    top: 90px;
    width: 22px;
    height: 22px;
    background: var(--ink-white);
  }

  .holder {
    position: absolute;
    right: 300px;
    top: 251px;
    margin: 0;
    font-family: "Mulish", sans-serif;
    font-weight: 800;
    font-size: 21px;
    color: var(--ink-black);
    white-space: nowrap;
  }
  .divider {
    position: absolute;
    left: 289px;
    top: 248px;
    width: 2px;
    height: 80px;
    background: var(--neon-orange);
  }
  .contact {
    position: absolute;
    left: 297px;
    top: 250px;
    margin: 0;
    padding: 0;
    list-style: none;
    font-family: "Mulish", sans-serif;
    font-weight: 400;
    font-size: 17px;
    line-height: 23px;
    color: var(--ink-white);
    white-space: nowrap;
  }
  .contact .indent { padding-left: 27px; }
</style>
</head>
<body>
  <main class="sheet">
    <section class="card card--front" aria-label="Card front">
      <span class="accent-square" aria-hidden="true"></span>
      <h1 class="wordmark">Gulvane</h1>
    </section>

    <section class="card card--back" aria-label="Card back">
      <span class="accent-square" aria-hidden="true"></span>
      <p class="wordmark">Gulvane</p>
      <p class="holder">Owen Carlisle Dray</p>
      <span class="divider" aria-hidden="true"></span>
      <ul class="contact">
        <li>e: owen@gulvane.example</li>
        <li>m: 555 318 6724</li>
        <li>w: gulvane.example</li>
        <li class="indent">gulvane-video.example</li>
      </ul>
    </section>
  </main>
</body>
</html>
```